Photographer Card

I'm currently doing freelance photography and i need a creative design name card especially when i attend events.
I require a design that makes a STATEMENT.
Simple, elegant and nothing like the usual name cards ive seen around (Example: with a camera/tripod etc in the design).

Photographer: Dorian VP
Mobile: +65 84126957
E-mail: Dorian.VP.Photography@mailvista.net
Friendlane: www.friendlane.net/dorian.vp.photography

Thanks for your time and hope it will turn out well! :)
Updates

Thanks for all your inputs!

Im liking the cursive feel.

Id prefer not to include the title "freelance"  :)

Also, im looking for a logo to establish myself

http://www.artmosaic.net/art/Cotton-Business-Card-583021746

Hi all! Thanks for the designs

"Capturing magical moments"
"Capturing magical moments that are gone forever"

Back design can be in big font "look HERE"

Maybe with focusing box 

Names can be played with horizontal and vertical.

Industry/Entity Type

Camera

Font styles to use
Script

```html
<!DOCTYPE html>
<html lang="en">
<head>
<meta charset="utf-8">
<title>Dorian VP Photography – Name Card</title>
<link rel="stylesheet" href="https://fonts.googleapis.com/css2?family=Cormorant+Garamond:wght@400;500&display=swap">
<style>
  :root {
    --page: #ffffff;
    --card-edge: #050505;
    --card-mid: #3a3a3a;
    --ink: #f4f4f4;
    --strip-dark: #151515;
    --strip-light: #8a8a8a;
  }
  html, body {
    margin: 0;
    padding: 0;
    width: 1200px;
    height: 1000px;
    overflow: hidden;
    background: var(--page);
  }
  .canvas {
    position: relative;
    width: 1200px;
    height: 1000px;
  }
  .card {
    position: absolute;
    left: 141px;
    top: 220px;
    width: 926px;
    height: 529px;
    background: radial-gradient(ellipse 60% 65% at 50% 48%, var(--card-mid) 0%, #1c1c1c 60%, var(--card-edge) 100%);
    overflow: hidden;
    font-family: "Cormorant Garamond", "Times New Roman", serif;
    color: var(--ink);
    text-align: center;
  }
  .film-band {
    position: absolute;
    left: 20px;
    right: 20px;
    height: 30px;
    background: linear-gradient(90deg, transparent 0%, var(--strip-light) 15%, #b8b8b8 50%, var(--strip-light) 85%, transparent 100%);
    opacity: 0.75;
  }
  .film-band::after {
    content: "";
    position: absolute;
    left: 0; right: 0;
    top: 9px;
    height: 12px;
    background: linear-gradient(90deg, transparent 0%, var(--strip-dark) 12%, var(--strip-dark) 88%, transparent 100%);
  }
  .film-band--top { top: 24px; }
  .film-band--bottom { bottom: 26px; }
  .tagline {
    position: absolute;
    top: 70px;
    left: 0; right: 0;
    margin: 0;
    font-size: 26px;
    font-weight: 400;
    letter-spacing: 1.6px;
    text-transform: uppercase;
    white-space: nowrap;
  }
  .brand-name {
    position: absolute;
    top: 150px;
    left: 0; right: 0;
    margin: 0;
    font-size: 110px;
    font-weight: 500;
    line-height: 1;
  }
  .contact {
    position: absolute;
    top: 322px;
    left: 0; right: 0;
    margin: 0;
    font-size: 30px;
    line-height: 33px;
    white-space: nowrap;
  }
  .contact__role {
    display: block;
    font-size: 36px;
    line-height: 40px;
  }
  .contact__line { display: block; }
</style>
</head>
<body>
<div class="canvas">
  <section class="card">
    <div class="film-band film-band--top" role="img" aria-label="Film strip border"></div>

    <p class="tagline">I'll shoot you! ,its okay, I'm a photographer!</p>

    <h1 class="brand-name">Dorian VP</h1>

    <p class="contact">
      <span class="contact__role">Photographer: Dorian VP</span>
      <span class="contact__line">Mobile: +65 84126957</span>
      <span class="contact__line">E-mail: Dorian.VP.Photography@mailvista.net</span>
      <span class="contact__line">Friendlane: www.friendlane.net/dorian.vp.photography</span>
    </p>

    <div class="film-band film-band--bottom" role="img" aria-label="Film strip border"></div>
  </section>
</div>
</body>
</html>
```